Medical group practice

We need a flyer design incorporating the three doctors in the practice, there is a general practitioner, ophthalmologist and an obstetrician & Gynaecologist. see the attached file for the concept. will leave the colour design up to you

Target Market(s)

general public

Industry/Entity Type

Health Care

Colors

Designer to choose colors to be used in the design.

Requirements
Must have
• logos included in attachement

```html
<!DOCTYPE html>
<html lang="en">
<head>
<meta charset="utf-8">
<title>Clearvale Medical – Flyer</title>
<link href="https://fonts.googleapis.com/css2?family=Baloo+2:wght@600;700&family=Dosis:wght@500;600&display=swap" rel="stylesheet">
<style>
  :root {
    --sky-top: #1f95ee;
    --sky-deep: #0c6fd8;
    --ring-blue: #1a8cf4;
    --pale: #dde8f1;
    --pale-shade: #c6d6e4;
    --ink: #1d2b42;
    --night: #1f1f21;
    --white: #ffffff;
  }
  html, body { margin: 0; padding: 0; overflow: hidden; }
  body { width: 855px; height: 1200px; background: var(--night); }
  .flyer {
    position: relative; width: 855px; height: 1200px; overflow: hidden;
    font-family: "Dosis", "Arial Narrow", sans-serif; color: var(--ink);
  }
  .backdrop { position: absolute; inset: 0; }
  .hours {
    position: absolute; left: 35px; top: 30px; margin: 0;
    font-size: 27px; font-weight: 500; line-height: 1.3; color: var(--ink);
  }
  .brand-mark {
    position: absolute; right: 30px; top: 70px;
    display: flex; align-items: center; gap: 8px;
    font-family: "Dosis", sans-serif; font-weight: 600; font-size: 20px;
    letter-spacing: 2px; color: var(--white);
  }
  .brand-mark .dot { width: 14px; height: 14px; border-radius: 50%; background: var(--white); }
  .title {
    position: absolute; left: 0; width: 100%; text-align: center; margin: 0;
    font-family: "Baloo 2", sans-serif; font-weight: 700; color: var(--ink);
  }
  .title--name { top: 252px; font-size: 74px; letter-spacing: 4px; line-height: 1; }
  .title--tagline { top: 372px; font-size: 70px; line-height: 1; font-weight: 600; }
  .address {
    position: absolute; top: 470px; width: 100%; text-align: center;
    font-size: 21px; font-weight: 500; margin: 0;
  }
  .service {
    position: absolute; top: 531px; width: 224px; height: 224px; border-radius: 50%;
    background: var(--ring-blue); box-sizing: border-box; padding: 9px;
  }
  .service__emblem {
    width: 100%; height: 100%; border-radius: 50%;
    background: radial-gradient(circle at 50% 40%, #58b3f5, #2c8fe6 75%);
  }
  .service--gp { left: 93px; }
  .service--eye { left: 315px; }
  .service--obgyn { left: 538px; }
  .direct-lines {
    position: absolute; top: 770px; left: 90px; width: 675px; text-align: center;
    margin: 0; font-size: 19px; font-weight: 600; line-height: 1.35;
  }
  .doctor {
    position: absolute; top: 928px; text-align: center; color: var(--white);
  }
  .doctor__name { margin: 0 0 22px; font-size: 22px; font-weight: 600; }
  .doctor__info, .doctor__services { margin: 0; font-size: 12.5px; font-weight: 500; line-height: 1.4; }
  .doctor__services { margin-top: 16px; }
  .doctor--gp { left: 40px; width: 250px; }
  .doctor--eye { left: 310px; width: 230px; }
  .doctor--obgyn { left: 565px; width: 250px; }
  .doctor--obgyn .doctor__name { margin-bottom: 26px; }
</style>
</head>
<body>
<div class="flyer">
  <svg class="backdrop" width="855" height="1200" viewBox="0 0 855 1200" aria-hidden="false">
    <defs>
      <linearGradient id="sky" x1="0" y1="0" x2="0" y2="1">
        <stop offset="0" stop-color="var(--sky-top)"/>
        <stop offset="1" stop-color="var(--sky-deep)"/>
      </linearGradient>
      <linearGradient id="paleFill" x1="0" y1="0" x2="1" y2="1">
        <stop offset="0" stop-color="#eaf1f7"/>
        <stop offset="0.55" stop-color="var(--pale)"/>
        <stop offset="1" stop-color="var(--pale-shade)"/>
      </linearGradient>
    </defs>
    <rect width="855" height="1200" fill="url(#sky)"/>
    <path d="M0 760 Q427 1040 855 760 L855 1200 L0 1200 Z" fill="var(--night)"/>
    <path d="M0 302 Q427 35 855 302 L855 720 Q427 985 0 720 Z" fill="none" stroke="#45a9f5" stroke-width="12"/>
    <path d="M0 302 Q427 35 855 302 L855 720 Q427 985 0 720 Z" fill="url(#paleFill)" role="img" aria-label="Soft-focus photo of a doctor holding a stethoscope"/>
  </svg>

  <p class="hours">Opening hours : Monday – Fridays 9am-6pm,<br>Saturdays 10am – 5pm</p>

  <div class="brand-mark"><span class="dot"></span>CLEARVALE</div>

  <h1 class="title title--name">CLEARVALE&nbsp; MEDICAL</h1>
  <p class="title title--tagline">Your Health is our Priority</p>
  <p class="address">42 Harbour Lane, Port Ellis, St. Verin Tel : (555) 410 2280 / 2281</p>

  <div class="service service--gp"><div class="service__emblem" role="img" aria-label="General practice emblem"></div></div>
  <div class="service service--eye"><div class="service__emblem" role="img" aria-label="Ophthalmology emblem"></div></div>
  <div class="service service--obgyn"><div class="service__emblem" role="img" aria-label="Obstetrics and gynaecology emblem"></div></div>

  <p class="direct-lines">General Practitioner - (555) 730 4412, Ophthalmologist - (555) 738 9065, Obstetrician/-<br>Gynaecologist – (555) 742 1186, (555) 619 3027</p>

  <section class="doctor doctor--gp">
    <h2 class="doctor__name">Dr. Leon Whitfield, MD</h2>
    <p class="doctor__info">General Practitioner<br>leon.whitfield.doc@example.com</p>
    <p class="doctor__services">General Checks<br>Annual Check ups<br>Wound Care/Dressings<br>Incision &amp; Drainage<br>Suturing lacerations<br>Pain Injections<br>Glucose checks<br>Foreign Body Removal</p>
  </section>

  <section class="doctor doctor--eye">
    <h2 class="doctor__name">Dr. Isabela R. Cortez</h2>
    <p class="doctor__info">MD. Surgeon Ophthalmologist<br>Email: isabela.doct@example.com</p>
    <p class="doctor__services">Eyes disease examination,<br>Surgery of Pterygium, Cataract,<br>Glaucoma, Emergency: Conjunctivitis,<br>Traumatism, Foreign body and more</p>
  </section>

  <section class="doctor doctor--obgyn">
    <h2 class="doctor__name">Dr. Kiran Malhotra,</h2>
    <p class="doctor__info">BMedSci, MBBS, DM (O&amp;G), FACOG<br>Obstetrician &amp; Gynaecologist<br>Email: drmalhotra@example.com</p>
    <p class="doctor__services">Obstetrics: Prenatal Care,<br>Delivery, Postnatal checks, High<br>Risk pregnancy Gynaecology : Pap smears,<br>Abnormal vaginal bleeding, Fibroids, Colpo-<br>scopy, Family planning, Infertility, Cancer<br>screening, And More....</p>
  </section>
</div>
</body>
</html>
```